Stone Harbor Group Business Card

We need a business card for our new office set-up in Switzerland. It's preferred to have someone who is familiar with the conventions for cards there (e.g. size is 85 X 54 mm). We are in the defense, security, and aerospace business. The website is brambleford.ch. Our logo is attached. The design should be sharp and conservative. It should be French on one side and English on the other.
Address is:
Rue des Tilleuls 27
1207 Genève
Target Market(s)
Senior professionals in governments, militaries, and defense industry.
Industry/Entity Type
Business
Contact Information for Business Card
Address, website address (www.stoneharbor.ch), email address, telephone, direct telephone, mobile phone.

```html
<!DOCTYPE html>
<html lang="en">
<head>
<meta charset="utf-8">
<title>Stone Harbor Group – Business Card</title>
<link rel="stylesheet" href="https://fonts.googleapis.com/css2?family=Cinzel:wght@500&family=Open+Sans:wght@400&display=swap">
<style>
  :root {
    --bg-light: #ffffff;
    --bg-dark: #b9b9b9;
    --card-top: #2a2a2a;
    --card-bottom: #0d0d0d;
    --red: #c0323f;
    --red-deep: #8e1f2a;
    --cream: #e9e0c8;
    --text-light: #d8d8d8;
    --flap: #3a3a3a;
  }
  html, body {
    margin: 0;
    width: 849px;
    height: 1200px;
    overflow: hidden;
  }
  body {
    position: relative;
    background: radial-gradient(ellipse at 50% 45%, var(--bg-light) 0%, #ececec 45%, var(--bg-dark) 100%);
  }
  .card {
    position: absolute;
    left: 125px;
    width: 591px;
    height: 382px;
    overflow: hidden;
    background: linear-gradient(180deg, var(--card-top), var(--card-bottom));
    box-shadow: 0 6px 14px rgba(0,0,0,0.35);
  }
  .card--front { top: 170px; }
  .card--back { top: 645px; }

  .brand-name {
    font-family: "Cinzel", serif;
    font-weight: 500;
    color: var(--red);
    font-size: 15px;
    letter-spacing: 1.5px;
    margin: 0;
  }
  .card--front .brand-name {
    position: absolute;
    left: 40px;
    top: 70px;
  }
  .card--front .brand-mark {
    position: absolute;
    left: 40px;
    top: 42px;
    width: 14px;
    height: 14px;
    background: var(--red);
  }

  .contact-list {
    position: absolute;
    left: 40px;
    top: 262px;
    margin: 0;
    padding: 0;
    list-style: none;
    font-family: "Open Sans", sans-serif;
    font-size: 11.5px;
    letter-spacing: 0.8px;
    text-transform: uppercase;
    color: var(--text-light);
    line-height: 19px;
  }
  .contact-list li { display: flex; align-items: center; gap: 7px; }
  .contact-list svg { width: 11px; height: 11px; fill: var(--text-light); flex: none; }

  .accent-shape {
    position: absolute;
    right: 0;
    bottom: 0;
    width: 330px;
    height: 382px;
  }

  .envelope-flap {
    position: absolute;
    inset: 0;
    width: 591px;
    height: 382px;
  }
  .card--back .brand-block {
    position: absolute;
    left: 0;
    right: 0;
    top: 175px;
    text-align: center;
  }
  .card--back .brand-name { font-size: 15px; }
</style>
</head>
<body>

<section class="card card--front" aria-label="Card front">
  <span class="brand-mark"></span>
  <p class="brand-name">Stone Harbor Group</p>

  <svg class="accent-shape" viewBox="0 0 330 382" role="img" aria-label="Large angular red decorative shape">
    <polygon points="330,40 330,382 120,382" fill="var(--cream)"/>
    <polygon points="330,58 330,382 140,382" fill="var(--red)"/>
  </svg>

  <ul class="contact-list">
    <li><svg viewBox="0 0 12 12"><path d="M6 0a4 4 0 0 0-4 4c0 3 4 8 4 8s4-5 4-8a4 4 0 0 0-4-4zm0 5.5A1.5 1.5 0 1 1 6 2.5a1.5 1.5 0 0 1 0 3z"/></svg>Rue des Tilleuls 27, 1207 Genève</li>
    <li><svg viewBox="0 0 12 12"><circle cx="6" cy="6" r="5" fill="none" stroke="var(--text-light)" stroke-width="1.2"/><path d="M1 6h10M6 1v10" stroke="var(--text-light)" stroke-width="1"/></svg>www.stoneharbor.ch</li>
    <li><svg viewBox="0 0 12 12"><path d="M2.5 0.5l2 2.5-1.2 1.5c.8 1.7 2.1 3 3.7 3.8L8.5 7l2.5 2-1.5 2.5C5 11 1 7 0.5 2z"/></svg>+41 (022) 555 01 27</li>
    <li><svg viewBox="0 0 12 12"><rect x="0.5" y="2" width="11" height="8" fill="none" stroke="var(--text-light)" stroke-width="1.1"/><path d="M0.5 2l5.5 4.5L11.5 2" fill="none" stroke="var(--text-light)" stroke-width="1.1"/></svg>contact@stoneharbor.ch</li>
  </ul>
</section>

<section class="card card--back" aria-label="Card back">
  <svg class="envelope-flap" viewBox="0 0 591 382" aria-hidden="true">
    <defs>
      <linearGradient id="flapShade" x1="0" y1="0" x2="0" y2="1">
        <stop offset="0" stop-color="#4a4a4a"/>
        <stop offset="1" stop-color="#1a1a1a"/>
      </linearGradient>
    </defs>
    <path d="M0 0 L591 0 L591 20 Q420 170 295 230 Q170 170 0 20 Z" fill="url(#flapShade)" opacity="0.75"/>
    <path d="M0 20 Q170 170 295 230 Q420 170 591 20" fill="none" stroke="#555" stroke-width="1"/>
  </svg>
  <div class="brand-block">
    <p class="brand-name">Stone Harbor Group</p>
  </div>
</section>

</body>
</html>
```